Commercial Loan Originator Business Card (CHANGE COLORS SCHEME)

CHANGE COLOR SCHEME - SAME DESIGN

Name Marissa Lantham
Title Commercial Loan Originator
Office (800) 641-2905 x68
Direct (240) 617-2435
Email brightleaf4you@mailpost.example

Name Derek Fallow
Office (800) 641-2905 x70
Direct (410) 932-1864
Email d.falthebroker@mailpost.example

Name Gordon Wexley
Office (800) 641-2905 x71
Direct (215) 346-2081
Email g.wexley37@mailpost.example

Name Lyn Moreau
Office (800) 641-2905 x
Direct (202) 458-1937
Email lmoreau64@mailpost.example

Name Nadia Strand
Office (800) 641-2905 x72
Direct (240) 871-5246
Email qrzhomelending@mailpost.example

```html
<!DOCTYPE html>
<html lang="en">
<head>
<meta charset="utf-8">
<title>Derek Fallow – Commercial Loan Originator Business Card</title>
<link rel="stylesheet" href="https://fonts.googleapis.com/css2?family=Cinzel:wght@600&family=Poppins:wght@400&display=swap">
<style>
  :root {
    --backdrop: #ececec;
    --card: #ffffff;
    --accent: #1f4e8c;
    --accent-soft: #d4e1f2;
    --ink: #1f1f1f;
    --portrait-light: #d9dcd6;
    --portrait-dark: #434b42;
  }
  html, body {
    margin: 0;
    width: 1200px;
    height: 952px;
    overflow: hidden;
    background: var(--backdrop);
  }
  .business-card {
    position: absolute;
    left: 0;
    top: 105px;
    width: 1200px;
    height: 742px;
    background: var(--card);
    overflow: hidden;
  }
  .corner-wedge {
    position: absolute;
    left: 0;
    top: 0;
  }
  .base-band {
    position: absolute;
    left: 0;
    bottom: 0;
    width: 100%;
    height: 18px;
    background: var(--accent);
  }
  .portrait {
    position: absolute;
    left: 730px;
    top: 91px;
    width: 420px;
    height: 633px;
    border-radius: 150px 150px 0 0;
    background: linear-gradient(180deg, var(--portrait-light) 0%, #7d857a 35%, var(--portrait-dark) 100%);
  }
  .contact-block {
    position: absolute;
    left: 51px;
    top: 0;
  }
  .person-name {
    position: absolute;
    left: 0;
    top: 386px;
    margin: 0;
    font-family: "Cinzel", serif;
    font-weight: 600;
    font-size: 53px;
    line-height: 1;
    color: var(--accent);
    white-space: nowrap;
  }
  .person-title {
    position: absolute;
    left: 0;
    top: 437px;
    margin: 0;
    font-family: "Poppins", sans-serif;
    font-size: 34px;
    line-height: 1;
    color: var(--ink);
    white-space: nowrap;
  }
  .contact-list {
    list-style: none;
    margin: 0;
    padding: 0;
  }
  .contact-item {
    position: absolute;
    left: 0;
    display: flex;
    align-items: center;
    font-family: "Poppins", sans-serif;
    font-size: 35px;
    line-height: 1;
    color: var(--ink);
    white-space: nowrap;
  }
  .contact-item.office { top: 538px; }
  .contact-item.direct { top: 581px; }
  .contact-item.email  { top: 626px; }
  .contact-icon {
    width: 34px;
    height: 34px;
    margin-right: 18px;
    flex: none;
  }
  .contact-item.email .contact-icon { margin-right: 25px; }
  .contact-label { color: var(--accent); margin-left: 12px; }
</style>
</head>
<body>
  <main class="business-card">
    <svg class="corner-wedge" width="770" height="200" viewBox="0 0 770 200" aria-hidden="true">
      <polygon points="0,116 760,0 0,193" fill="var(--accent-soft)"/>
      <polygon points="0,0 754,0 0,116" fill="var(--accent)"/>
    </svg>

    <div class="portrait" role="img" aria-label="Portrait photo of Derek Fallow in a dark green suit"></div>

    <section class="contact-block">
      <h1 class="person-name">DEREK FALLOW</h1>
      <p class="person-title">Commercial Loan Originator</p>
      <ul class="contact-list">
        <li class="contact-item office">
          <svg class="contact-icon" viewBox="0 0 24 24" aria-hidden="true">
            <path d="M6.6 3.5c.5-.5 1.3-.5 1.8 0l2.2 2.6c.4.5.4 1.2 0 1.7L9.3 9.2c.9 2 2.9 4.1 5 5.1l1.4-1.3c.5-.4 1.2-.4 1.700l2.6 2.2c.5.5.5 1.3 0 1.8l-1.7 1.7c-.9.9-2.3 1.1-3.4.5C10 17 6.9 13.8 5 9.2c-.5-1.2-.3-2.5.6-3.4z" fill="none" stroke="var(--accent)" stroke-width="1.8"/>
            <path d="M14 3.5a7 7 0 0 1 6.5 6.5M14 7a3.5 3.5 0 0 1 3 3" fill="none" stroke="var(--accent)" stroke-width="1.8" stroke-linecap="round"/>
          </svg>
          <span>(800) 641-2905 x70</span>
        </li>
        <li class="contact-item direct">
          <svg class="contact-icon" viewBox="0 0 24 24" aria-hidden="true">
            <path d="M6.6 3.5c.5-.5 1.3-.5 1.8 0l2.2 2.6c.4.5.4 1.2 0 1.7L9.3 9.2c.9 2 2.9 4.1 5 5.1l1.4-1.3c.5-.4 1.2-.4 1.7 0l2.6 2.2c.5.5.5 1.3 0 1.8l-1.7 1.7c-.9.9-2.3 1.1-3.4.5C10 17 6.9 13.8 5 9.2c-.5-1.2-.3-2.5.6-3.4z" fill="none" stroke="var(--accent)" stroke-width="1.8"/>
            <path d="M14 3.5a7 7 0 0 1 6.5 6.5M14 7a3.5 3.5 0 0 1 3 3" fill="none" stroke="var(--accent)" stroke-width="1.8" stroke-linecap="round"/>
          </svg>
          <span>(410) 932-1864</span><span class="contact-label">(Direct )</span>
        </li>
        <li class="contact-item email">
          <svg class="contact-icon" viewBox="0 0 24 24" aria-hidden="true">
            <rect x="1" y="5" width="22" height="14" fill="var(--accent)"/>
            <path d="M1 5l11 8 11-8M1 19l8-7M23 19l-8-7" fill="none" stroke="#ffffff" stroke-width="1.4"/>
          </svg>
          <span>d.falthebroker@mailpost.example</span>
        </li>
      </ul>
    </section>

    <div class="base-band"></div>
  </main>
</body>
</html>
```